正面とサイドの看板をお願いします。
その際に看板・買い物袋・名刺・ハンコに使用するロゴもお願いします。
焼きたてパン工房 みさと
天然酵母・北海道産小麦使用・無添加生地
看板の色は決まっていません。
店内は、白を基調としてカウンターや棚等は白っぽいアンティーク調な木材を使用する予定です。
店内から工房も見えるようにします。工房の壁は薄いピンクか薄いブルーにします。
添付してある資料は、あくまでも素人の私が勝手に制作したものですので、これとは全く別の提案をお願いします。
素材等もNetから拾った物ですので使用できません。
店舗イメージを追加しました。
質問に対してお答えいたします。
1)「みさと」のネーミングの意味or由来をお教え下さい。
>みさとという名前は、お店を切り盛りしていく娘夫婦の子供の名前です。
2)「みさと」ロゴ作成時のテイストですが、あえてお選び頂くならば【柔らかく優しい雰囲気】or【スッキリしたオシャレな雰囲気】ではどちらがご希望でしょうか?
>スッキリしたオシャレな雰囲気でお願いします。
3)看板にイラストor写真を使用するとしたらどちらがお好みですか?
イラストが好みです。
4)看板全体の色使いですが、ぱっと見で【目立つ】ことと、お店全体の雰囲気との【調和】ではどちらをご希望でしょうか?
>お店全体の雰囲気との【調和】を希望します。

全体に優しそうで温もりが感じられました。
文字と色のバランスやイラストも素晴らしく、とても気に入りました。

沢山の応募をしてくださり、誠にありがとうございました。
どれも良い作品ばかりで、とても悩みました。
今回は、選考に漏れた方にはお詫び申し上げます。
皆様の今後のご活躍をお祈りしております。
本当にありがとうございました。

```html
<!DOCTYPE html>
<html lang="ja">
<head>
<meta charset="UTF-8">
<title>焼きたてパン工房 みさと 看板</title>
<link rel="stylesheet" href="https://fonts.googleapis.com/css2?family=Shippori+Mincho+B1:wght@700;800&family=Zen+Maru+Gothic:wght@500;700;900&display=swap">
<style>
  :root {
    --paper: #ffffff;
    --ink: #3a2b22;
    --brand-red: #8e1b22;
    --accent-orange: #e4421c;
    --wheat-gold: #e2c27a;
    --wheat-faint: #f4ead2;
    --bread: #e9a53f;
  }
  html, body {
    margin: 0;
    padding: 0;
    width: 855px;
    height: 1200px;
    overflow: hidden;
    background: var(--paper);
  }
  .signboard {
    position: relative;
    width: 855px;
    height: 1200px;
    background: var(--paper);
    overflow: hidden;
  }
  .wheat-art {
    position: absolute;
  }
  .wheat-top {
    left: 300px; top: 48px; width: 255px; height: 50px;
    background: linear-gradient(90deg, rgba(226,194,122,0), var(--wheat-gold) 30%, var(--wheat-gold) 70%, rgba(226,194,122,0));
    border-radius: 25px;
    opacity: 0.75;
  }
  .wheat-divider {
    left: 250px; top: 560px; width: 355px; height: 44px;
    background: linear-gradient(90deg, rgba(226,194,122,0), var(--wheat-gold) 30%, var(--wheat-gold) 70%, rgba(226,194,122,0));
    border-radius: 22px;
    opacity: 0.75;
  }
  .wheat-left {
    left: 0; top: 600px; width: 210px; height: 600px;
    background: linear-gradient(180deg, rgba(244,234,210,0), var(--wheat-faint) 35%, var(--wheat-faint));
    border-top-right-radius: 140px;
  }
  .wheat-right {
    right: 0; top: 640px; width: 170px; height: 520px;
    background: linear-gradient(180deg, rgba(244,234,210,0), var(--wheat-faint) 40%, rgba(244,234,210,0.6));
    border-top-left-radius: 120px;
  }
  .bread-art {
    left: 318px; top: 1072px; width: 220px; height: 92px;
    background: radial-gradient(ellipse at 50% 40%, #f3c36a, var(--bread) 60%, #c9802b);
    border-radius: 46px;
  }
  .shop-tagline {
    position: absolute;
    top: 102px; left: 0; width: 100%;
    margin: 0;
    text-align: center;
    font-family: "Zen Maru Gothic", sans-serif;
    font-weight: 700;
    font-size: 42px;
    letter-spacing: 2px;
    color: var(--ink);
  }
  .shop-name {
    position: absolute;
    top: 200px; left: 0; width: 100%;
    margin: 0;
    text-align: center;
    font-family: "Shippori Mincho B1", serif;
    font-weight: 800;
    font-size: 230px;
    line-height: 300px;
    letter-spacing: 10px;
    color: var(--brand-red);
  }
  .shop-name-roman {
    position: absolute;
    top: 496px; left: 0; width: 100%;
    margin: 0;
    text-align: center;
    font-family: "Zen Maru Gothic", sans-serif;
    font-weight: 500;
    font-size: 44px;
    letter-spacing: 30px;
    text-indent: 30px;
    color: var(--brand-red);
  }
  .features {
    position: absolute;
    top: 668px; left: 0; width: 100%;
    margin: 0; padding: 0;
    list-style: none;
    text-align: center;
    font-family: "Zen Maru Gothic", sans-serif;
    font-weight: 900;
    font-size: 64px;
    line-height: 100px;
    letter-spacing: 4px;
    color: var(--accent-orange);
  }
</style>
</head>
<body>
  <main class="signboard">
    <div class="wheat-art wheat-left" role="img" aria-label="麦の穂のイラスト(左)"></div>
    <div class="wheat-art wheat-right" role="img" aria-label="麦の穂のイラスト(右)"></div>
    <div class="wheat-art wheat-top" role="img" aria-label="麦の穂の飾り"></div>

    <p class="shop-tagline">焼きたてパン工房</p>
    <h1 class="shop-name">みさと</h1>
    <p class="shop-name-roman">MISATO</p>

    <div class="wheat-art wheat-divider" role="img" aria-label="麦の穂の区切り飾り"></div>

    <ul class="features">
      <li>北海道産小麦使用</li>
      <li>天然酵母</li>
      <li>無添加生地</li>
    </ul>

    <div class="wheat-art bread-art" role="img" aria-label="フランスパンのイラスト"></div>
  </main>
</body>
</html>
```